Tarvin Year 9 Curriculum Model

We need a graphic that communicates all the overlapping elements of our new curriculum. Perhaps it could involve a series of concentric circles moving out from the centre:
1. the "Ideal Learner" profile at the centre with the school's logo behind it (see uploaded file).
2. The words of the "General Capabilities" from the Australian national curriculum in the next circle moving out of centre: "Ethical Understanding" "Literacy" "Numeracy" "Intercultural Awareness" "ICT Capacity" "Critical and Creative Thinking" "Personal and Social Capability"
3. Next circle out has the subjects: "Mathematics" "English" "Languages" "Health and Physical Education" "Technology" "Religious Education" "Humanities" "Arts" "Science"
4. Next Circle out has the title "Community" and then less important, the words "Local" "Regional" "National"
5. Next circle out is simple called "World"
6. Next circle out is simply called "Future"
IF there is a way to make it look not too bad...:Overlaying all the other aspects, floating somewhere, are the 3 significant priorities for the curriculum: Asia, Indigenous Culture and Sustainability

Target Market(s)

Year 9 (15 year old) school students and their parents, as well as teachers and other visitors to the school. It will be used to explain the curriculum and have on the walls as a reminder.

Industry/Entity Type

School

Requirements
Must have
• All of the words in the brief, with a relational dimension for each.

```html
<!DOCTYPE html>
<html lang="en">
<head>
<meta charset="utf-8">
<title>Tarvin Year 9 Curriculum Model</title>
<link rel="stylesheet" href="https://fonts.googleapis.com/css2?family=Quicksand:wght@500;600;700&display=swap">
<style>
  :root {
    --page: #ffffff;
    --future: #1d3557;
    --world: #457b9d;
    --community: #e9c46a;
    --subjects: #2a9d8f;
    --capabilities: #264653;
    --core: #f4a261;
    --ring-text: #f7f4ec;
    --community-text: #4a3300;
    --core-text: #1d3557;
    --bubble: #ffffff;
    --asia: #1d3557;
    --sustain: #9c2f12;
    --indigenous: #14532d;
  }
  html, body {
    margin: 0;
    padding: 0;
    overflow: hidden;
    background: var(--page);
  }
  .canvas {
    width: 1200px;
    height: 1000px;
    position: relative;
    overflow: hidden;
    background: var(--page);
  }
  .curriculum-model {
    display: block;
    width: 1200px;
    height: 1000px;
    font-family: "Quicksand", sans-serif;
  }
  .ring-future { fill: var(--future); }
  .ring-world { fill: var(--world); }
  .ring-community { fill: var(--community); }
  .ring-subjects { fill: var(--subjects); }
  .ring-capabilities { fill: var(--capabilities); }
  .ring-core { fill: var(--core); }
  .ring-title {
    font-size: 24px;
    font-weight: 600;
    letter-spacing: 5px;
    fill: var(--ring-text);
  }
  .community-title { fill: var(--community-text); }
  .community-place {
    font-size: 14px;
    font-weight: 600;
    fill: var(--community-text);
  }
  .subject {
    font-size: 15px;
    font-weight: 600;
    fill: var(--ring-text);
  }
  .capability {
    font-size: 14px;
    font-weight: 600;
    fill: var(--ring-text);
  }
  .core-label {
    font-size: 22px;
    font-weight: 700;
    letter-spacing: 1px;
    fill: var(--core-text);
  }
  .priority-disc {
    fill: var(--bubble);
    fill-opacity: 0.72;
    stroke: var(--bubble);
    stroke-width: 3;
  }
  .priority-label {
    font-size: 18px;
    font-weight: 700;
  }
  .priority-asia { fill: var(--asia); }
  .priority-sustainability { fill: var(--sustain); }
  .priority-indigenous { fill: var(--indigenous); }
</style>
</head>
<body>
<div class="canvas">
<svg class="curriculum-model" viewBox="0 0 1200 1000" xmlns="http://www.w3.org/2000/svg" role="img" aria-label="Tarvin Year 9 curriculum model: concentric rings around the ideal learner">
  <defs>
    <path id="cw-406" d="M600,903 A406,406 0 1 1 600,91 A406,406 0 1 1 600,903"/>
    <path id="ccw-406" d="M600,91 A406,406 0 1 0 600,903 A406,406 0 1 0 600,91"/>
    <path id="cw-333" d="M600,830 A333,333 0 1 1 600,164 A333,333 0 1 1 600,830"/>
    <path id="cw-260" d="M600,757 A260,260 0 1 1 600,237 A260,260 0 1 1 600,757"/>
    <path id="ccw-260" d="M600,237 A260,260 0 1 0 600,757 A260,260 0 1 0 600,237"/>
    <path id="cw-200" d="M600,697 A200,200 0 1 1 600,297 A200,200 0 1 1 600,697"/>
    <path id="ccw-200" d="M600,297 A200,200 0 1 0 600,697 A200,200 0 1 0 600,297"/>
    <path id="cw-165" d="M600,662 A165,165 0 1 1 600,332 A165,165 0 1 1 600,662"/>
    <path id="ccw-165" d="M600,332 A165,165 0 1 0 600,662 A165,165 0 1 0 600,332"/>
    <path id="cw-124" d="M600,621 A124,124 0 1 1 600,373 A124,124 0 1 1 600,621"/>
    <path id="ccw-124" d="M600,373 A124,124 0 1 0 600,621 A124,124 0 1 0 600,373"/>
    <path id="cw-92" d="M600,589 A92,92 0 1 1 600,405 A92,92 0 1 1 600,589"/>
    <path id="ccw-92" d="M600,405 A92,92 0 1 0 600,589 A92,92 0 1 0 600,405"/>
  </defs>

  <g class="rings">
    <circle class="ring-future" cx="600" cy="497" r="443"/>
    <circle class="ring-world" cx="600" cy="497" r="369"/>
    <circle class="ring-community" cx="600" cy="497" r="297"/>
    <circle class="ring-subjects" cx="600" cy="497" r="222"/>
    <circle class="ring-capabilities" cx="600" cy="497" r="146"/>
    <circle class="ring-core" cx="600" cy="497" r="70"/>
  </g>

  <g class="ring-labels" text-anchor="middle" dominant-baseline="central">
    <text class="ring-title"><textPath href="#ccw-406" startOffset="63.9%">FUTURE</textPath></text>
    <text class="ring-title"><textPath href="#cw-333" startOffset="36.4%">WORLD</textPath></text>
    <text class="ring-title community-title"><textPath href="#cw-260" startOffset="50%">COMMUNITY</textPath></text>
    <text class="community-place"><textPath href="#cw-260" startOffset="75%">Local</textPath></text>
    <text class="community-place"><textPath href="#ccw-260" startOffset="50%">Regional</textPath></text>
    <text class="community-place"><textPath href="#cw-260" startOffset="25%">National</textPath></text>
  </g>

  <g class="subject-labels" text-anchor="middle" dominant-baseline="central">
    <text class="subject"><textPath href="#cw-200" startOffset="50.8%">Technology</textPath></text>
    <text class="subject"><textPath href="#cw-165" startOffset="63.9%">Mathematics</textPath></text>
    <text class="subject"><textPath href="#cw-200" startOffset="75%">Religious Education</textPath></text>
    <text class="subject"><textPath href="#ccw-165" startOffset="60.8%">Languages</textPath></text>
    <text class="subject"><textPath href="#ccw-200" startOffset="50%">Humanities</textPath></text>
    <text class="subject"><textPath href="#ccw-165" startOffset="38.6%">English</textPath></text>
    <text class="subject"><textPath href="#ccw-200" startOffset="31.1%">Arts</textPath></text>
    <text class="subject"><textPath href="#cw-200" startOffset="33.1%">Science</textPath></text>
    <text class="subject"><textPath href="#cw-165" startOffset="34.7%">Health and Physical Education</textPath></text>
  </g>

  <g class="capability-labels" text-anchor="middle" dominant-baseline="central">
    <text class="capability"><textPath href="#cw-124" startOffset="33.3%">Intercultural Awareness</textPath></text>
    <text class="capability"><textPath href="#cw-124" startOffset="60.3%">ICT Capacity</textPath></text>
    <text class="capability"><textPath href="#cw-92" startOffset="72.2%">Ethical Understanding</textPath></text>
    <text class="capability"><textPath href="#ccw-124" startOffset="63.1%">Critical and Creative Thinking</textPath></text>
    <text class="capability"><textPath href="#ccw-92" startOffset="50.6%">Literacy</textPath></text>
    <text class="capability"><textPath href="#ccw-124" startOffset="38.3%">Numeracy</textPath></text>
    <text class="capability"><textPath href="#cw-92" startOffset="25%">Personal and Social Capability</textPath></text>
  </g>

  <g class="core-labels" text-anchor="middle">
    <text class="core-label" x="600" y="479">Ideal</text>
    <text class="core-label" x="600" y="504">Tarvin</text>
    <text class="core-label" x="600" y="529">Learner</text>
  </g>

  <g class="priority priority-asia-group">
    <circle class="priority-disc" cx="832" cy="241" r="88"/>
    <text class="priority-label priority-asia" x="832" y="248" text-anchor="middle">ASIA</text>
  </g>
  <g class="priority priority-sustainability-group">
    <circle class="priority-disc" cx="263" cy="409" r="88"/>
    <text class="priority-label priority-sustainability" x="263" y="416" text-anchor="middle">SUSTAINABILITY</text>
  </g>
  <g class="priority priority-indigenous-group">
    <circle class="priority-disc" cx="753" cy="810" r="88"/>
    <text class="priority-label priority-indigenous" x="753" y="806" text-anchor="middle">INDIGENOUS</text>
    <text class="priority-label priority-indigenous" x="753" y="834" text-anchor="middle">CULTURE</text>
  </g>
</svg>
</div>
</body>
</html>
```